Design my dad a new business card because his current one sucks!

I need a business card designed for my fathers home maintenance business. His customers are individuals (single moms, old people etc.) as well as the occasional business. As such it needs to be accessible to both target audiences.

The front of the card should be dark grey on yellow with the logo and contain the following information:
- Warren Dobrinski
- 0487 362 914
- info@harbourlinehandyworks.com.au
- 0487 362 914

- ABN: 87 214 630 592
- 'Fully Insured'

The reverse should be yellow on dark grey and will have the web address:
- harbourlinehandyworks.com.au

And a few key services he offers:
GENERAL REPAIRS
PAINTING/TILING/
PAVING &CONCRETING
PRESSURE WASHING
ON-SITE WELDING
DECKING ADDITIONS & REPAIRS
FENCING
FULL BOND CLEANING

This will be first time the logo has been printed so you will need to come up with the best CMYK approximation of the RGB colours to make sure it is a close as possible.

```html
<!DOCTYPE html>
<html lang="en">
<head>
<meta charset="utf-8">
<title>Harbourline Handyworks – Business Card</title>
<link href="https://fonts.googleapis.com/css2?family=Open+Sans:wght@400;600;700&display=swap" rel="stylesheet">
<style>
  :root {
    --stage: #d9d6d1;
    --charcoal: #272525;
    --charcoal-deep: #1e1c1c;
    --yellow: #f1d51f;
    --yellow-deep: #e6b80f;
    --ink: #231f20;
  }
  * { box-sizing: border-box; margin: 0; padding: 0; }
  html, body {
    width: 1200px; height: 723px; overflow: hidden;
    background: var(--stage);
    font-family: "Open Sans", sans-serif;
  }
  .stage {
    width: 1200px; height: 723px;
    display: flex; align-items: center; justify-content: center; gap: 80px;
  }
  .card {
    width: 370px; height: 620px;
    position: relative;
    box-shadow: 0 12px 30px rgba(0,0,0,.25);
  }

  /* Reverse */
  .card-back {
    background: linear-gradient(160deg, var(--charcoal), var(--charcoal-deep));
    color: var(--yellow);
    text-align: center;
  }
  .service-list {
    list-style: none;
    padding-top: 70px;
    font-size: 15px; font-weight: 400; letter-spacing: .3px;
    line-height: 38px;
  }
  .card-back .brand {
    position: absolute; left: 0; right: 0; top: 445px;
    color: var(--yellow);
  }
  .web-address {
    position: absolute; left: 0; right: 0; bottom: 48px;
    font-size: 17px; font-weight: 400;
  }

  /* Front */
  .card-front {
    background: linear-gradient(150deg, var(--yellow) 35%, var(--yellow-deep));
    color: var(--ink);
    padding: 48px 34px 0;
  }
  .brand {
    font-weight: 700; line-height: 1;
    display: flex; flex-direction: column; align-items: center;
  }
  .brand-name { font-size: 44px; letter-spacing: -1px; }
  .brand-sub { font-size: 17px; letter-spacing: 3px; text-transform: uppercase; margin-top: 4px; }
  .card-front .brand { color: var(--ink); }
  .holder-name {
    margin-top: 58px;
    font-size: 31px; font-weight: 700; text-align: center;
  }
  .contact {
    margin-top: 46px; text-align: center;
    font-size: 15px; font-weight: 600; line-height: 30px;
  }
  .contact .email { font-size: 14px; }
  .insured {
    margin-top: 52px; text-align: center;
    font-size: 32px; font-weight: 400;
  }
  .abn {
    margin-top: 22px; text-align: center;
    font-size: 16px; font-weight: 600;
  }
</style>
</head>
<body>
<main class="stage">
  <section class="card card-back" aria-label="Card reverse">
    <ul class="service-list">
      <li>GENERAL REPAIRS</li>
      <li>PAINTING/TILING/</li>
      <li>PAVING &amp;CONCRETING</li>
      <li>PRESSURE WASHING</li>
      <li>ON-SITE WELDING</li>
      <li>DECKING ADDITIONS &amp; REPAIRS</li>
      <li>FENCING</li>
      <li>FULL BOND CLEANING</li>
    </ul>
    <div class="brand">
      <span class="brand-name">harbourline</span>
      <span class="brand-sub">handyworks</span>
    </div>
    <p class="web-address">www.harbourlinehandyworks.com.au</p>
  </section>

  <section class="card card-front" aria-label="Card front">
    <div class="brand">
      <span class="brand-name">harbourline</span>
      <span class="brand-sub">handyworks</span>
    </div>
    <h1 class="holder-name">Warren Dobrinski</h1>
    <div class="contact">
      <p class="phone">0487 362 914</p>
      <p class="email">info@harbourlinehandyworks.com.au</p>
      <p class="phone">0487 362 914</p>
    </div>
    <p class="insured">Fully Insured</p>
    <p class="abn">ABN: 87 214 630 592</p>
  </section>
</main>
</body>
</html>
```